Business Card Design For Marketing Agnecy LVT

Need business card design for marketing agency.

Dorian Pell
President, CEO
1-555-304-2917
dorian@lumenvaletrewards.net
www.LumenValeTrewards.biz

Back Side:
Boost Sales Using Rewards, Incentives & Giveaways
Get A Free Sample Package

Target Market(s)

B2B

Industry/Entity Type

Marketing

Contact Information for Business Card

Dorian Pell
President, CEO
1-555-304-2917

Back Side:
Get A Free Sample Package

Please note that my current url is OLD DESIGN. I am working on new design and want the business card to match color themes at least on new site. Here is the demo link for new site so you can see the colors I use, etc.

http://pagekilnstudio.example/qx/dorian/lvt_final/index.html

Requirements
Must have
• Please note that my current url is OLD DESIGN. I am working on new design and want the business card to match color themes at least on new site. Here is the demo link for new site so you can see the colors I use, etc.

Nice to have

Should not have

```html
<!DOCTYPE html>
<html lang="en">
<head>
<meta charset="utf-8">
<title>LVT Business Card</title>
<link href="https://fonts.googleapis.com/css2?family=Montserrat:wght@500;700&family=Oswald:wght@500;700&family=Kaushan+Script&family=Roboto:wght@400;700&display=swap" rel="stylesheet">
<style>
  :root {
    --brand-blue: #337bc1;
    --brand-grey: #5b5c5f;
    --paper: #f4f4f4;
    --backdrop: #e8e8e8;
    --ink: #3d3d3d;
    --white: #ffffff;
  }
  * { margin: 0; padding: 0; box-sizing: border-box; }
  html, body {
    width: 1199px; height: 1200px; overflow: hidden;
    background: var(--backdrop);
    font-family: "Roboto", Arial, sans-serif;
  }
  .canvas { position: relative; width: 1199px; height: 1200px; }

  /* Brand wordmark */
  .brand-mark {
    position: absolute; top: 90px; left: 0; width: 100%;
    display: flex; justify-content: center; align-items: center; gap: 22px;
  }
  .brand-mark .dot { width: 34px; height: 34px; border-radius: 50%; background: var(--brand-blue); }
  .brand-mark .name {
    font-family: "Montserrat", sans-serif; font-weight: 700;
    font-size: 180px; line-height: 1; letter-spacing: 4px; color: var(--brand-blue);
  }

  /* Cards */
  .card {
    position: absolute; width: 500px; height: 286px;
    border-radius: 18px; overflow: hidden; background: var(--paper);
    box-shadow: 0 14px 28px rgba(0,0,0,0.14);
  }
  .card-back { left: 70px; top: 520px; }
  .card-front { left: 629px; top: 620px; }

  .card-back .shapes { position: absolute; inset: 0; }
  .card-back .mini-mark {
    position: absolute; left: 22px; top: 188px;
    display: flex; align-items: center; gap: 6px;
  }
  .mini-mark .dot { width: 8px; height: 8px; border-radius: 50%; background: var(--brand-blue); }
  .mini-mark .name {
    font-family: "Montserrat", sans-serif; font-weight: 700; font-size: 26px; color: var(--brand-blue);
  }
  .pitch {
    position: absolute; left: 236px; top: 28px; width: 250px; color: var(--white);
  }
  .pitch .lead {
    font-family: "Montserrat", sans-serif; font-weight: 500; font-size: 14px; letter-spacing: 1px;
  }
  .pitch .headline {
    font-family: "Oswald", sans-serif; font-weight: 700; font-size: 34px;
    line-height: 1; text-transform: uppercase; letter-spacing: 1px;
  }
  .pitch .offer {
    font-family: "Kaushan Script", cursive; font-size: 22px; margin-top: 8px; white-space: nowrap;
  }
  .pitch .url { font-weight: 700; font-size: 11.5px; margin-top: 6px; white-space: nowrap; }

  /* Front */
  .card-front .edge-band {
    position: absolute; right: 0; top: 0; width: 16px; height: 100%;
    background: linear-gradient(to bottom, var(--brand-grey) 0 22%, var(--brand-blue) 22% 100%);
  }
  .card-front .logo-block {
    position: absolute; left: 30px; top: 0; width: 190px; height: 100%;
    display: flex; align-items: center; justify-content: center; gap: 10px;
  }
  .logo-block .dot { width: 14px; height: 14px; border-radius: 50%; background: var(--brand-blue); }
  .logo-block .name {
    font-family: "Montserrat", sans-serif; font-weight: 700; font-size: 60px; color: var(--brand-blue);
  }
  .card-front .divider {
    position: absolute; left: 232px; top: 56px; width: 1px; height: 174px; background: var(--brand-grey);
  }
  .contact { position: absolute; left: 252px; top: 74px; color: var(--ink); }
  .contact .person { font-weight: 700; font-size: 22px; color: var(--brand-blue); }
  .contact .role { font-weight: 700; font-size: 12px; margin: 4px 0 12px; }
  .contact ul { list-style: none; }
  .contact li {
    display: flex; align-items: center; gap: 7px; font-size: 10.5px; margin-bottom: 7px;
  }
  .contact li svg { width: 12px; height: 12px; fill: var(--brand-grey); flex: none; }
</style>
</head>
<body>
<div class="canvas">

  <header class="brand-mark">
    <span class="name">LVT</span>
    <span class="dot"></span>
  </header>

  <section class="card card-back">
    <svg class="shapes" viewBox="0 0 500 286" preserveAspectRatio="none">
      <polygon points="150,0 166,0 208,286 192,286" fill="var(--brand-grey)"/>
      <polygon points="176,0 500,0 500,286 218,286" fill="var(--brand-blue)"/>
    </svg>
    <div class="mini-mark"><span class="name">LVT</span><span class="dot"></span></div>
    <div class="pitch">
      <p class="lead">BOOST SALES USING</p>
      <p class="headline">Rewards<br>Incentives<br>&amp; Giveaways</p>
      <p class="offer">Get a free sample package</p>
      <p class="url">www.LumenValeTrewards.biz</p>
    </div>
  </section>

  <section class="card card-front">
    <div class="logo-block"><span class="name">LVT</span><span class="dot"></span></div>
    <div class="divider"></div>
    <div class="contact">
      <p class="person">Dorian Pell</p>
      <p class="role">President, CEO</p>
      <ul>
        <li>
          <svg viewBox="0 0 24 24"><path d="M6.6 10.8a15.1 15.1 0 0 0 6.6 6.6l2.2-2.2a1 1 0 0 1 1-.25 11.4 11.4 0 0 0 3.6.57 1 1 0 0 1 1 1V20a1 1 0 0 1-1 1A17 17 0 0 1 3 4a1 1 0 0 1 1-1h3.5a1 1 0 0 1 1 1c0 1.25.2 2.45.57 3.57a1 1 0 0 1-.25 1z"/></svg>
          1-555-304-2917
        </li>
        <li>
          <svg viewBox="0 0 24 24"><path d="M2 5h20v14H2z M3 6l9 7 9-7" stroke="var(--paper)" stroke-width="1.5"/></svg>
          dorian@lumenvaletrewards.net
        </li>
        <li>
          <svg viewBox="0 0 24 24"><circle cx="12" cy="12" r="10"/><path d="M2 12h20M12 2c3 3 3 17 0 20M12 2c-3 3-3 17 0 20" stroke="var(--paper)" stroke-width="1.5" fill="none"/></svg>
          www.LumenValeTrewards.biz
        </li>
      </ul>
    </div>
    <div class="edge-band"></div>
  </section>

</div>
</body>
</html>
```